KLV Messaging - veteran and exclusive boutique copywriting agency

PROJECT NEEDS:
1. Website design - full homepage design and inner page top banner design
2. Logo design
* Please see attached Briefs (Word Docs) for descriptions of what is needed for 1 and 2 above.
ABOUT THE CLIENT:
KLV Messaging is a veteran and exclusive boutique copywriting agency run by Marcus Holloway. Marcus is an award-winning published novelist and an accomplished executive ghostwriter with articles regularly published prominent technology publications like Brisk, ByteHarbor, FoundryPulse, and more. For nearly three decades, Marcus has focused solely on the technology sector - serving clients in Israel, Europe and the US.

Target Market(s)

hi-tech companies run by serious, confident professionals.

Industry/Entity Type

Business

Number of Pages Required

2 page

Font styles to use
Sans Serif
Other font styles liked:
• font should be modern

Colors
0054AA
0677BA
7BADD7
CADEEF
E8F1F8
F0912C
F2A743
F7CA91
FBE8D2
FDF5EE

Requirements
Must have
• psd files for logo, homepage design, and inner page top banner design
Nice to have
• Please see attached Website and Logo Design Briefs (Word Docs)
Should not have

```html
<!DOCTYPE html>
<html lang="en">
<head>
<meta charset="utf-8">
<title>KLV Messaging — The Art of Business Communication</title>
<link rel="stylesheet" href="https://fonts.googleapis.com/css2?family=Anton&family=Montserrat:ital,wght@0,400;0,500;0,600;0,700;0,800;1,400;1,600;1,700&display=swap">
<style>
:root{
  --navy:#243b6b;
  --navy-deep:#1c2f57;
  --orange:#f9a72b;
  --orange-dark:#f0912c;
  --slate:#6d8bb0;
  --grey:#e4e4e4;
  --ink:#2a2a2a;
  --muted:#4a4a4a;
  --white:#ffffff;
}
*{box-sizing:border-box;margin:0;padding:0}
html,body{width:1200px;height:5254px;overflow:hidden}
body{font-family:"Montserrat",sans-serif;color:var(--ink);background:var(--white)}
.page{position:relative;width:1200px;height:5254px;overflow:hidden;background:var(--white)}
.abs{position:absolute}
.wave{position:absolute;left:0;width:1200px;display:block}
.btn{position:absolute;display:flex;align-items:center;justify-content:center;background:var(--orange);color:var(--white);font-size:12px;font-weight:500;border-radius:16px}
.photo{position:absolute}

/* header */
.brand{left:163px;top:12px;color:var(--navy);font-weight:800;line-height:1}
.brand .mark{font-size:52px;letter-spacing:2px;display:block}
.brand .word{font-size:14px;letter-spacing:3.4px;display:block;margin-top:4px}
.nav{left:512px;top:38px;display:flex;gap:24px;font-size:12px;font-weight:500;text-transform:uppercase;color:#333}
.nav .active{color:var(--orange)}
.nav-contact{left:938px;top:30px;width:100px;height:32px}

/* hero */
.hero-arc{left:-160px;top:-190px;width:440px;height:440px;border:26px solid #eeeff2;border-radius:50%}
.hero-title{left:163px;top:166px;font-family:"Anton",sans-serif;font-size:82px;line-height:86px;color:var(--orange);letter-spacing:1px}
.hero-sub{left:163px;top:340px;width:380px;font-size:14px;line-height:25px;color:var(--ink)}
.hero-btn{left:163px;top:412px;width:98px;height:30px}
.hero-photo{left:690px;top:100px;width:300px;height:560px;border-radius:120px 120px 20px 20px;background:linear-gradient(180deg,#c9b8a8 0%,#9fb7d6 30%,#7f9ec6 60%,#3f5273 100%)}

/* clients */
.clients{left:180px;top:836px;width:850px;height:44px;display:flex;justify-content:space-between;align-items:center;font-weight:700;font-size:20px}
.arrow{position:absolute;width:26px;height:26px;border:1.5px solid #555;border-radius:50%;display:flex;align-items:center;justify-content:center}
.client{display:flex;align-items:center;gap:8px}
.client .dot{width:14px;height:14px;border-radius:50%}

/* frames */
.frame{position:absolute;background:var(--white);border-radius:70px 0 70px 0;box-shadow:0 10px 30px rgba(0,0,0,.15);padding:16px}
.frame .photo{position:relative;width:100%;height:100%;border-radius:56px 0 56px 0}

.h2{position:absolute;font-size:36px;font-weight:500;color:#111;line-height:1.15}
.kicker{position:absolute;color:var(--orange);font-style:italic;font-size:13px;line-height:24px}
.body{position:absolute;font-size:13px;line-height:24px;color:var(--muted)}
.body p+p{margin-top:24px}

/* services */
.grey-block{position:absolute;left:0;width:1200px;background:var(--grey)}
.card{position:absolute;z-index:2;top:1652px;width:269px;height:250px;background:var(--slate);border-radius:6px;text-align:center;color:var(--white);padding:80px 12px 0}
.card h3{color:var(--orange);font-size:18px;font-weight:600;line-height:22px}
.card h4{font-size:12.5px;font-weight:600;margin-top:6px;line-height:18px}
.card p{font-size:12.5px;line-height:24px;margin-top:6px}
.icon-ring{position:absolute;top:-68px;left:67px;width:135px;height:135px;border-radius:50%;background:var(--orange-dark);border:5px solid var(--white);display:flex;align-items:center;justify-content:center;box-shadow:0 6px 14px rgba(0,0,0,.18)}

/* why */
.why-item{position:absolute;left:160px;width:380px;display:flex;gap:22px}
.why-item svg{flex:none}
.why-item p{font-size:12.5px;line-height:24px;color:#222}

/* testimonial */
.quote{left:282px;top:2968px;width:648px;height:163px;background:var(--white);border-bottom:5px solid var(--orange);box-shadow:0 6px 20px rgba(0,0,0,.08);text-align:center;padding:40px 40px 0}
.quote p{font-style:italic;font-size:12.5px;line-height:24px;color:#222}
.quote .who{font-style:normal;font-weight:600;font-size:11.5px;margin-top:12px}

/* footer */
.footer{position:absolute;left:0;top:4990px;width:1200px;height:202px;background:var(--navy);color:var(--white)}
.f-title{position:absolute;font-size:13px;font-weight:600}
.f-list{position:absolute;font-size:12px;line-height:31px}
.f-list .current{text-decoration:underline}
.f-item{position:absolute;display:flex;gap:12px;font-size:12px;line-height:25px}
.f-brand{position:absolute;left:785px;top:28px;width:256px;text-align:center;font-weight:800;color:var(--white);line-height:1}
.f-brand .mark{font-size:62px;letter-spacing:4px;display:block}
.f-brand .word{font-size:14px;font-weight:500;display:block;margin-top:8px;letter-spacing:.3px}
.socials{position:absolute;left:866px;top:160px;display:flex;gap:6px}
.socials span{width:24px;height:24px;border-radius:50%;background:#1f8ad1;border:2px solid var(--white)}
.copyright{position:absolute;left:0;top:5192px;width:1200px;height:62px;background:var(--navy-deep);color:var(--white);font-size:11.5px;display:flex;align-items:center;justify-content:center}
</style>
</head>
<body>
<div class="page">

  <!-- header -->
  <div class="abs hero-arc"></div>
  <div class="abs brand"><span class="mark">KLV</span><span class="word">MESSAGING</span></div>
  <nav class="abs nav"><span class="active">Home</span><span>About</span><span>Industries</span><span>Portfolio</span><span>Clients</span></nav>
  <div class="btn nav-contact">Contact</div>

  <!-- hero -->
  <h1 class="abs hero-title">YOUR VOICE,<br>MY WORDS.</h1>
  <p class="abs hero-sub">Copywriting and executive ghostwriting that speaks for your vision and your technology.</p>
  <div class="btn hero-btn">Contact</div>

  <svg class="wave" style="top:470px;height:260px" viewBox="0 0 1200 260" preserveAspectRatio="none">
    <path d="M0,40 C200,120 420,150 650,112 C860,78 1010,28 1200,58 L1200,118 C1010,100 860,150 650,168 C420,188 200,150 0,96 Z" fill="var(--orange)"/>
    <path d="M0,96 C200,150 420,188 650,168 C860,150 1010,100 1200,118 L1200,146 C1000,150 820,196 600,226 C380,258 170,262 0,206 Z" fill="var(--navy)"/>
  </svg>
  <div class="photo hero-photo" role="img" aria-label="Portrait of Marcus Holloway standing in a light blue shirt and jeans"></div>

  <!-- clients -->
  <div class="arrow" style="left:98px;top:846px"><svg width="10" height="10" viewBox="0 0 10 10"><path d="M6.5 1.5 3 5l3.5 3.5" fill="none" stroke="#555" stroke-width="1.5"/></svg></div>
  <div class="abs clients">
    <span class="client" style="color:#1b4f9c">Pulsar Net</span>
    <span class="client" style="color:#2b5fa8"><span class="dot" style="background:#2b5fa8"></span>Corvane</span>
    <span class="client" style="color:#e8741c">Voltera</span>
    <span class="client" style="color:#3e4450">Nexomi</span>
    <span class="client" style="color:#8e3a8f"><span class="dot" style="background:#8e3a8f"></span>Trilune</span>
    <span class="client" style="color:#1d7a4a">Veridian Med</span>
  </div>
  <div class="arrow" style="left:1068px;top:846px"><svg width="10" height="10" viewBox="0 0 10 10"><path d="M3.5 1.5 7 5 3.5 8.5" fill="none" stroke="#555" stroke-width="1.5"/></svg></div>

  <!-- what I do -->
  <div class="frame" style="left:163px;top:1030px;width:408px;height:480px">
    <div class="photo" role="img" aria-label="Portrait of Marcus Holloway seated in a grey sweater against a dark backdrop" style="background:linear-gradient(160deg,#3a3a3a 0%,#1c1c1c 45%,#2f3d52 100%)"></div>
  </div>
  <h2 class="h2" style="left:624px;top:1036px">What I do</h2>
  <p class="abs" style="left:624px;top:1084px;color:var(--orange);font-size:20px;font-weight:500">The Art Of Business Communication</p>
  <div class="body" style="left:624px;top:1126px;width:420px">
    <p>Lorem ipsum dolor sit amet, consectetuer adipiscing elit, sed diam nonummy nibh euismod tincidunt ut laoreet dolore magna aliquam erat volutpat. Ut wisi enim ad minim veniam, corper suscipit lobortis nisl ut aliquip ex ea commodo consequat.</p>
    <p>Duis autem vel eum iriure dolor in hendrerit in vulputate velit esse molestie consequat, vel illum dolore eu feugiat nulla facilisis .</p>
  </div>

  <!-- services -->
  <svg class="wave" style="top:1380px;height:142px" viewBox="0 0 1200 142" preserveAspectRatio="none">
    <path d="M0,70 C300,130 520,140 800,112 C1000,92 1100,44 1200,22 L1200,142 L0,142 Z" fill="var(--grey)"/>
    <path d="M700,124 C900,104 1080,52 1200,0 L1200,34 C1100,70 960,112 800,122 Z" fill="var(--navy)"/>
  </svg>
  <div class="grey-block" style="top:1520px;height:320px"></div>

  <svg class="wave" style="top:1836px;height:170px" viewBox="0 0 1200 170" preserveAspectRatio="none">
    <path d="M0,0 H1200 V60 C1000,20 800,40 600,90 C400,140 200,110 0,70 Z" fill="var(--grey)"/>
    <path d="M0,70 C200,110 400,140 600,90 C800,40 1000,20 1200,60 V96 C1000,64 800,96 600,140 C400,182 200,160 0,118 Z" fill="var(--orange)"/>
  </svg>

  <div class="card" style="left:161px">
    <div class="icon-ring"><svg width="64" height="64" viewBox="0 0 64 64" fill="none" stroke="#fff" stroke-width="2.5"><rect x="6" y="10" width="36" height="26" rx="4"/><path d="M14 36v8l8-8"/><rect x="20" y="22" width="38" height="26" rx="4" fill="var(--orange-dark)"/><path d="M48 48v8l-8-8"/></svg></div>
    <h3>Messaging</h3><h4>The Value of a Fresh Perspective</h4>
    <p>Could you be reaching farther? Clearly-defined, accurately-targeted messaging is crucial.</p>
  </div>
  <div class="card" style="left:465px">
    <div class="icon-ring"><svg width="64" height="64" viewBox="0 0 64 64" fill="none" stroke="#fff" stroke-width="2.5"><path d="M14 6h26l10 10v28"/><path d="M14 6v46h20"/><path d="M20 20h16M20 28h20M20 36h12"/><circle cx="46" cy="48" r="10"/><path d="M41 48l4 4 6-7"/></svg></div>
    <h3>Collateral</h3><h4>Concise, Effective, Creative</h4>
    <p>Marketing collateral that effectively communicates who you are and what you want to say.</p>
  </div>
  <div class="card" style="left:769px">
    <div class="icon-ring"><svg width="64" height="64" viewBox="0 0 64 64" fill="none" stroke="#fff" stroke-width="2.5"><path d="M10 14h26v42H10z"/><path d="M16 24h14M16 32h14M16 40h10"/><path d="M30 30 58 12 46 46 40 34z"/><path d="M40 34 58 12"/></svg></div>
    <h3>Content Marketing</h3><h4>Giving Voice to Your Vision</h4>
    <p>Articles, blog content, white papers, e-books. Your ideas and expertise, our words.</p>
  </div>

  <!-- why choose me -->
  <h2 class="h2" style="left:161px;top:2082px">Why Choose Me</h2>
  <p class="kicker" style="left:161px;top:2128px;width:440px">In nearly two decades in the international marketing trenches, I've learned to rapidly define and internalize company messages - and to communicate them at eye-level.</p>

  <div class="why-item" style="top:2244px">
    <svg width="66" height="66" viewBox="0 0 66 66" fill="none" stroke="#2b3b5c" stroke-width="2"><circle cx="22" cy="18" r="8" fill="#fbe8d2"/><circle cx="44" cy="18" r="8" fill="#fbe8d2"/><path d="M8 50v-12a10 10 0 0 1 10-10h8a10 10 0 0 1 10 10v12"/><path d="M30 50v-12a10 10 0 0 1 10-10h8a10 10 0 0 1 10 10v12"/><path d="M4 50h58"/></svg>
    <p>I do all client writing myself, so my clients get <b>one-on-one service</b> and a <b>personal guarantee of quality.</b></p>
  </div>
  <div class="why-item" style="top:2364px">
    <svg width="66" height="66" viewBox="0 0 66 66" fill="none" stroke="#2b3b5c" stroke-width="2"><rect x="16" y="12" width="34" height="44" rx="4" fill="#fbe8d2"/><path d="M26 12l7 9 7-9"/><path d="M33 21v24"/><path d="M29 30l4-4 4 4"/></svg>
    <p>My writing is <b>concise, elegant,</b> and <b>professional</b> - while at the same time reflecting an understated creativity and sense of humor that brings company messages to a very intimate, personal level.</p>
  </div>
  <div class="why-item" style="top:2530px">
    <svg width="66" height="66" viewBox="0 0 66 66" fill="none" stroke="#2b3b5c" stroke-width="2"><path d="M18 30a10 10 0 0 1 6-18 12 12 0 0 1 22 2 9 9 0 0 1 2 16z" fill="#fbe8d2"/><path d="M33 30v12M22 30v8l-8 8M44 30v8l8 8M33 42v10"/><circle cx="12" cy="50" r="4"/><circle cx="54" cy="50" r="4"/><circle cx="33" cy="56" r="4"/></svg>
    <p>I offer clients a <b>deep understanding of business, communication, and technology</b> - coupled with a hard-hitting and concise, yet elegant writing style.</p>
  </div>
  <div class="btn" style="left:247px;top:2662px;width:98px;height:30px">Contact</div>

  <div class="photo" role="img" aria-label="Portrait of Marcus Holloway standing with arms crossed in a grey long-sleeve shirt" style="left:612px;top:2040px;width:337px;height:700px;border-radius:140px 140px 0 0;background:linear-gradient(180deg,#d8c7b8 0%,#5b6068 25%,#4d5258 60%,#4d6a92 100%)"></div>

  <!-- testimonials -->
  <svg class="wave" style="top:2720px;height:152px" viewBox="0 0 1200 152" preserveAspectRatio="none">
    <path d="M0,60 C200,140 420,60 700,30 C900,10 1100,20 1200,40 V152 H0 Z" fill="var(--grey)"/>
    <path d="M0,12 C150,62 300,130 520,84 C320,150 110,130 0,80 Z" fill="var(--navy)"/>
  </svg>
  <div class="grey-block" style="top:2870px;height:340px"></div>
  <h2 class="h2" style="left:0;width:1200px;text-align:center;top:2896px">What They’re Saying</h2>
  <div class="arrow" style="left:240px;top:3044px"><svg width="10" height="10" viewBox="0 0 10 10"><path d="M6.5 1.5 3 5l3.5 3.5" fill="none" stroke="#555" stroke-width="1.5"/></svg></div>
  <div class="abs quote">
    <p>Marcus is a terrific resource for our company. A self-starter, who has generated a great deal of revenue for us and does high-quality work. Highly recommended.</p>
    <p class="who">Noam Vardi, CEO, Harbor Shield</p>
  </div>
  <div class="arrow" style="left:946px;top:3044px"><svg width="10" height="10" viewBox="0 0 10 10"><path d="M3.5 1.5 7 5 3.5 8.5" fill="none" stroke="#555" stroke-width="1.5"/></svg></div>

  <svg class="wave" style="top:3200px;height:190px" viewBox="0 0 1200 190" preserveAspectRatio="none">
    <path d="M0,0 H1200 V40 C1000,10 820,70 600,110 C400,150 200,120 0,70 Z" fill="var(--grey)"/>
    <path d="M0,70 C200,120 400,150 600,110 C820,70 1000,10 1200,40 V80 C1000,60 820,110 600,150 C400,190 200,170 0,110 Z" fill="var(--orange)"/>
  </svg>

  <!-- about -->
  <div class="frame" style="left:163px;top:3462px;width:408px;height:536px">
    <div class="photo" role="img" aria-label="Portrait of Marcus Holloway in a brown jacket against a dark backdrop" style="background:linear-gradient(160deg,#2a2a2a 0%,#1a1a1a 45%,#6b4a30 100%)"></div>
  </div>
  <h2 class="h2" style="left:608px;top:3500px">About Marcus<br>Holloway</h2>
  <p class="kicker" style="left:608px;top:3592px;width:440px;font-weight:600">In nearly two decades in the international marketing trenches, I've learned to rapidly define and internalize company messages - and to communicate them at eye-level.</p>
  <div class="body" style="left:608px;top:3672px;width:420px">
    <p>Born and raised in the US, I've lived and worked in Israel since 1990, and speak fluent Hebrew. I do all client writing myself, so my clients get one-on-one service and a personal guarantee of quality.</p>
    <p>My writing is concise, elegant, and professional - while at the same time reflecting an understated creativity and sense of humor that brings company messages to a very intimate, personal level. I offer clients a deep understanding of business, communication, and technology - coupled with a hard-hitting and concise, yet elegant writing style.</p>
  </div>

  <!-- author -->
  <svg class="wave" style="top:4030px;height:90px" viewBox="0 0 1200 90" preserveAspectRatio="none">
    <path d="M0,60 C300,10 600,0 850,30 C1000,48 1100,70 1200,60 V90 H0 Z" fill="var(--grey)"/>
  </svg>
  <div class="grey-block" style="top:4118px;height:780px"></div>
  <h2 class="h2" style="left:163px;top:4196px">Marcus’s Work<br>As An Author</h2>
  <p class="abs" style="left:163px;top:4288px;color:var(--navy);font-style:italic;font-weight:700;font-size:12.5px;line-height:24px">Writer, Dad, Musician, Gardener...<br>Not Necessarily in that Order</p>
  <div class="body" style="left:163px;top:4348px;width:440px;color:#222">
    <p>I was born in 1967 near Austin Texas, and grew up uneventfully in Fort Wayne, Indiana - birthplace of Dana Whitfield, and fictional home of the Field Station character Hal Brenner, among others. When you grow up in a place like Fort Wayne, any claim to fame is important...</p>
    <p>After completing my BA at Lakeshore University - during the course of which I also studied at Northgate University and Harborview University - I emigrated to Israel only months before the first Gulf War, in August 1990. In between planeloads of immigrants from the former Soviet Union, I was given an Israeli ID card and a gas mask, in that order. I'm still not sure which one of these ultimately produced greater headaches.</p>
  </div>
  <div class="btn" style="left:163px;top:4714px;width:112px;height:30px">Read More</div>

  <div class="frame" style="left:632px;top:4162px;width:404px;height:470px">
    <div class="photo" role="img" aria-label="Portrait of Marcus Holloway smiling in a white shirt against a dark blue backdrop" style="background:linear-gradient(160deg,#1f2f52 0%,#2c3d66 50%,#d9d9d9 100%)"></div>
  </div>
  <div class="photo" role="img" aria-label="Covers of two novels by Marcus Holloway" style="left:690px;top:4600px;width:300px;height:260px;background:linear-gradient(120deg,#2a2a2a 0%,#555 45%,#c49a5a 55%,#6d5a45 100%);border-radius:4px"></div>

  <!-- footer -->
  <svg class="wave" style="top:4840px;height:160px" viewBox="0 0 1200 160" preserveAspectRatio="none">
    <path d="M0,0 H1200 V90 C1000,40 800,20 560,60 C340,96 150,100 0,70 Z" fill="var(--grey)"/>
    <path d="M0,70 C150,100 340,96 560,60 C800,20 1000,40 1200,90 V160 H0 Z" fill="var(--orange)"/>
    <path d="M0,84 C150,116 340,112 560,76 C800,38 1000,56 1200,104 V160 H0 Z" fill="var(--navy)"/>
  </svg>
  <footer class="footer">
    <p class="f-title" style="left:163px;top:24px">Quick Links</p>
    <div class="f-list" style="left:163px;top:54px"><span class="current">Home</span><br>About<br>Services<br>Industries</div>
    <div class="f-list" style="left:263px;top:54px">Portfolio<br>Clients<br>Contact</div>
    <p class="f-title" style="left:522px;top:24px">Contact Us</p>
    <div class="f-item" style="left:522px;top:58px">
      <svg width="14" height="18" viewBox="0 0 14 18"><path d="M7 1a6 6 0 0 1 6 6c0 4.5-6 10-6 10S1 11.5 1 7a6 6 0 0 1 6-6z" fill="none" stroke="var(--orange)" stroke-width="1.6"/><circle cx="7" cy="7" r="2" fill="var(--orange)"/></svg>
      <span>P.O. Box 1187<br>Elmwood 40215</span>
    </div>
    <div class="f-item" style="left:522px;top:118px">
      <svg width="16" height="14" viewBox="0 0 16 14"><rect x="1" y="2" width="14" height="10" fill="none" stroke="var(--orange)" stroke-width="1.6"/><path d="M1 2l7 6 7-6" fill="none" stroke="var(--orange)" stroke-width="1.6"/></svg>
      <span>hello@klvmessaging.example</span>
    </div>
    <div class="f-item" style="left:522px;top:152px">
      <svg width="12" height="18" viewBox="0 0 12 18"><rect x="1" y="1" width="10" height="16" rx="2" fill="none" stroke="var(--orange)" stroke-width="1.6"/><path d="M4 14h4" stroke="var(--orange)" stroke-width="1.6"/></svg>
      <span style="font-weight:600">+1-555-018-2740</span>
    </div>
    <div class="f-brand"><span class="mark">KLV</span><span class="word">THE ART OF BUSINESS COMMUNICATION</span></div>
    <div class="socials" aria-label="Social profiles"><span></span><span></span><span></span></div>
  </footer>
  <div class="copyright">© 2023 KLV The Art of Business Communication. All Right Reserved.</div>

</div>
</body>
</html>
```